Plakat-Design für kleine deutsche Immobilien- und Reiseveranstalter-Firma
Zielgruppe
Kleine deutsche Immobilien- und Reiseveranstalter-Firma, spezialisiert auf Italien. In Italien sind es Immobilienbesitzer, die aus versch. Gründen hoffen an Ausländer zu verkaufen/vermieten ( Alter ca. ab 35-40)
Aufgabenstellung
Um neue Immo-Besitzer anzusprechen, lassen wir in verschiedenen Gemeinden in der Nordtoskana Plakate gegen Gebühr kleben ( 70 x 100, meistens 1 bis 2 Wochen)
Text auf Italienisch
Was an Text rein muss( falls Sie es anders mitteilen wollen, bin ich gerne bereit es zu diskutieren)
VUOI VENDERE CASA A STRANIERI O AFFITTARLA A TURISTI ? (Übersetzung ca.:= wollen Sie Ihre Immobilie an Ausländer verkaufen oder an Touristen vermieten?)
Verdora
Germania – info@verdora-beispiel.de + 49 7412 3804417
Italia – 0573 – 214096, Cell.: 381 – 2097461, 337- 42 90586,
www.verdorahomes-beispiel.com
www.verdorarentals-beispiel.com
Der Poster, den man meistens im Vorbeifahren sieht, soll springt sofort ins Auge , fast aufdringlich. Man kann mit Farben oder Bildern (oder beiden) arbeiten. Stechende Farben, sonst minimalistisch einfach. (??)
Erfahrung zeigt, daß die beiden Mobile Nummern (Cell.:) mehr sichtbar sein könnten. Ich kann zwei letzte zeigen, aber ungern, weil sie mir nicht gefallen und Neues – besseres suche.
PS: habe mal so was wie Guerilla -Marketing versucht – wurde nicht verstanden.
Bilder kann ich nach Wunsch liefern.

```html
<!DOCTYPE html>
<html lang="it">
<head>
<meta charset="utf-8">
<title>Vuoi vendere casa a stranieri o affittarla a turisti? – Verdora</title>
<link rel="stylesheet" href="https://fonts.googleapis.com/css2?family=Outfit:wght@700;800;900&display=swap">
<style>
  :root {
    --cream: #fcf9e5;
    --green: #5ba246;
    --sky: #72bfe8;
    --ink: #111111;
    --white: #ffffff;
    --flag-red: #d62d24;
    --flag-gold: #fde93c;
    --flag-green: #5aa146;
  }
  html, body {
    margin: 0;
    padding: 0;
    overflow: hidden;
    background: var(--cream);
  }
  .poster {
    position: relative;
    width: 838px;
    height: 1200px;
    overflow: hidden;
    background: var(--cream);
    font-family: "Outfit", Arial, sans-serif;
    color: var(--ink);
  }
  .headline {
    margin: 0;
    font-weight: 900;
    color: var(--green);
  }
  .headline span {
    position: absolute;
    left: 52px;
    line-height: 1;
    white-space: nowrap;
    letter-spacing: -1px;
  }
  .line-vuoi { top: 124px; font-size: 83px; }
  .line-vendere { top: 209px; font-size: 77px; color: var(--sky); }
  .line-casa { top: 295px; font-size: 126px; }
  .line-stranieri { top: 421px; font-size: 82px; }
  .line-affittarla { top: 512px; font-size: 116px; letter-spacing: -2px; }
  .line-turisti { top: 633px; font-size: 120px; letter-spacing: -2px; }

  .megaphone-art {
    position: absolute;
    left: 580px;
    top: 205px;
    width: 224px;
    height: 289px;
    border-radius: 8px;
    background: linear-gradient(160deg, #e6eef0 0%, #cfe6f2 45%, #d9d9d2 100%);
  }
  .divider {
    position: absolute;
    left: 47px;
    top: 787px;
    width: 757px;
    height: 2px;
    background: var(--ink);
  }
  .phone-icon {
    position: absolute;
    left: 330px;
    top: 844px;
    width: 110px;
    height: 140px;
  }
  .flag {
    position: absolute;
    left: 45px;
    width: 80px;
    height: 80px;
  }
  .flag-de { top: 958px; }
  .flag-it { top: 1072px; }
  .contact {
    position: absolute;
    left: 147px;
    margin: 0;
    font-weight: 800;
    white-space: nowrap;
    line-height: 1;
  }
  .contact-email { top: 974px; font-size: 19px; font-weight: 700; }
  .contact-de-phone { top: 1004px; font-size: 38px; }
  .contact-it-phone { top: 1079px; font-size: 37px; }
  .contact-it-mobile { top: 1119px; font-size: 37px; }
  .contact-rule {
    position: absolute;
    left: 47px;
    top: 1053px;
    width: 375px;
    height: 2px;
    background: var(--ink);
  }
  .brand-disc {
    position: absolute;
    left: 482px;
    top: 887px;
    width: 470px;
    height: 470px;
    border-radius: 50%;
    background: var(--white);
    border: 5px solid var(--green);
    box-sizing: border-box;
  }
  .brand-name {
    position: absolute;
    left: 556px;
    top: 1030px;
    margin: 0;
    font-size: 60px;
    font-weight: 800;
    line-height: 1;
    color: var(--ink);
    white-space: nowrap;
  }
  .brand-web {
    position: absolute;
    left: 557px;
    top: 1108px;
    margin: 0;
    font-size: 15px;
    font-weight: 800;
    line-height: 1.5;
    white-space: nowrap;
  }
</style>
</head>
<body>
<main class="poster">
  <h1 class="headline">
    <span class="line-vuoi">VUOI</span>
    <span class="line-vendere">VENDERE</span>
    <span class="line-casa">CASA A</span>
    <span class="line-stranieri">STRANIERI O</span>
    <span class="line-affittarla">AFFITTARLA</span>
    <span class="line-turisti">A TURISTI?</span>
  </h1>

  <div class="megaphone-art" role="img" aria-label="Illustrazione: persona che annuncia con un megafono azzurro"></div>

  <div class="divider"></div>

  <svg class="phone-icon" viewBox="0 0 110 140" aria-hidden="true">
    <rect x="30" y="4" width="62" height="112" rx="9" fill="none" stroke="#111" stroke-width="3"/>
    <line x1="52" y1="12" x2="70" y2="12" stroke="#111" stroke-width="3" stroke-linecap="round"/>
    <path d="M30 50 C18 58 14 80 10 102 L4 116" fill="none" stroke="#111" stroke-width="3" stroke-linecap="round"/>
    <path d="M92 116 C80 130 60 134 44 134" fill="none" stroke="#111" stroke-width="3" stroke-linecap="round"/>
  </svg>

  <svg class="flag flag-de" viewBox="0 0 80 80" aria-label="Germania" role="img">
    <defs><clipPath id="clip-de"><circle cx="40" cy="40" r="40"/></clipPath></defs>
    <g clip-path="url(#clip-de)">
      <rect x="0" y="0" width="80" height="27" fill="#111"/>
      <rect x="0" y="27" width="80" height="27" fill="var(--flag-red)"/>
      <rect x="0" y="54" width="80" height="26" fill="var(--flag-gold)"/>
    </g>
  </svg>
  <p class="contact contact-email">info@verdora-beispiel.de</p>
  <p class="contact contact-de-phone">49 74 12 38 04 417</p>

  <div class="contact-rule"></div>

  <svg class="flag flag-it" viewBox="0 0 80 80" aria-label="Italia" role="img">
    <defs><clipPath id="clip-it"><circle cx="40" cy="40" r="40"/></clipPath></defs>
    <g clip-path="url(#clip-it)">
      <rect x="0" y="0" width="27" height="80" fill="var(--flag-green)"/>
      <rect x="27" y="0" width="26" height="80" fill="var(--white)"/>
      <rect x="53" y="0" width="27" height="80" fill="var(--flag-red)"/>
    </g>
  </svg>
  <p class="contact contact-it-phone">0573 – 214 096</p>
  <p class="contact contact-it-mobile">381 – 20 97 461</p>

  <div class="brand-disc"></div>
  <p class="brand-name">Verdora</p>
  <p class="brand-web">www.verdorahomes-beispiel.com<br>www.verdorarentals-beispiel.com</p>
</main>
</body>
</html>
```